WERBE-FLYER
Zielgruppe
Immobilien Makler
Aufgabenstellung
Überarbeitung des bestehenden Entwurfs.
Der Flyer wird an Hauseigentümer mit der Post verteilt (nicht adressierte Werbung).
Format:
offen A4 Querformat
geschlossen (1x gefaltet) A5 (4 Seiten)
In der Mitte eine Perforationslinie zum Abtrennen. Danach kann die Seite 3 & 4 zusammengefaltet (geklebt) werden und an uns zurückgeschickt werden.
Rücksendung erfolgt via Geschäftsantwortsendung - ohne Strichcode (siehe Vorlage Alpin. Kurier).

```html
<!DOCTYPE html>
<html lang="de">
<head>
<meta charset="utf-8">
<title>NOVERA Immobilien – Werbe-Flyer</title>
<link href="https://fonts.googleapis.com/css2?family=Arimo:wght@400;700&display=swap" rel="stylesheet">
<style>
  :root{
    --navy:#1b3a5c;
    --ink:#3c3c3c;
    --muted:#6b6b6b;
    --paper:#ffffff;
    --tape:#e6e6e7;
    --bg:#ffffff;
  }
  *{box-sizing:border-box;margin:0;padding:0}
  html,body{width:1200px;height:490px;overflow:hidden;background:var(--bg)}
  body{font-family:"Arimo",Arial,sans-serif;color:var(--ink);position:relative}

  .sheet{position:absolute;top:34px;width:548px;height:392px;background:var(--paper);
    box-shadow:0 1px 4px rgba(0,0,0,.18);overflow:hidden}
  .sheet--outside{left:32px}
  .sheet--inside{left:594px}

  /* ---------- Outside: reply side ---------- */
  .reply-side{position:absolute;left:0;top:0;width:274px;height:392px}
  .reply-mark{position:absolute;left:132px;top:14px;display:flex;align-items:flex-start;gap:8px}
  .reply-mark__letter{font-size:26px;line-height:26px;color:#111}
  .reply-mark__note{font-size:3.6px;line-height:5px;color:#111;margin-top:8px}
  .reply-mark__type{position:absolute;left:132px;top:44px;font-size:3.4px;line-height:4.6px;color:#111;width:130px}
  .reply-address{position:absolute;left:149px;top:94px;font-size:6.4px;line-height:8px;color:#333;font-style:normal}

  /* ---------- Outside: cover ---------- */
  .cover{position:absolute;left:274px;top:0;width:274px;height:392px;
    background:linear-gradient(180deg,#f7f7f8 0%,#f0f0f1 100%)}
  .brand{display:flex;align-items:center;gap:6px}
  .brand__square{width:20px;height:20px;background:var(--navy)}
  .brand__name{font-weight:400;color:var(--navy);letter-spacing:.5px;line-height:1}
  .cover .brand{position:absolute;right:24px;top:38px}
  .cover .brand__square{width:26px;height:26px}
  .cover .brand__name{font-size:19px}
  .cover__photo{position:absolute;left:0;top:92px;width:274px;height:191px;
    background:linear-gradient(180deg,#aebdcc 0%,#d8dde2 35%,#e8e9ea 55%,#b9b4ab 80%,#8f877c 100%)}
  .cover__tagline{position:absolute;left:0;width:274px;top:306px;text-align:center;
    font-size:13.5px;color:var(--navy)}
  .cover__band{position:absolute;left:0;bottom:0;width:274px;height:44px;background:var(--navy);
    display:flex;align-items:center;justify-content:center}
  .cover__url{color:#fff;font-size:8.5px;border-bottom:.6px solid #fff;padding-bottom:1px}

  /* ---------- Inside: services ---------- */
  .services{position:absolute;left:27px;top:0;width:226px;height:392px}
  .bar{position:absolute;left:0;width:226px;height:15px;background:var(--navy);color:#fff;
    font-size:8.4px;font-weight:400;line-height:15px;padding-left:4px}
  .bar--services{top:28px}
  .bar--sale{top:54px}
  .bar--valuation{top:168px}
  .copy{position:absolute;left:0;width:226px;font-size:4.4px;line-height:5.6px;color:var(--muted)}
  .copy--sale{top:73px}
  .copy--valuation{top:188px}
  .bullets{position:absolute;left:12px;width:210px;font-size:4.4px;line-height:5.6px;color:var(--muted);list-style:disc}
  .bullets--sale{top:101px}
  .bullets--valuation{top:218px}
  .services .brand{position:absolute;left:4px;top:277px}
  .services .brand__square{width:17px;height:17px}
  .services .brand__name{font-size:15px}
  .contact{position:absolute;left:12px;top:309px;font-size:5.8px;line-height:7.7px;color:#333;font-style:normal}

  .perforation{position:absolute;left:273px;top:0;height:392px;width:0;border-left:1px dashed #888}

  /* ---------- Inside: reply card ---------- */
  .reply-card{position:absolute;left:297px;top:0;width:226px;height:392px}
  .tape{position:absolute;left:0;width:226px;height:19px;background:var(--tape);color:#fff;
    font-size:4.2px;line-height:19px;text-align:center}
  .tape--top{top:0}
  .tape--bottom{bottom:0}
  .reply-card__title{position:absolute;left:0;top:59px;font-size:8.4px;font-weight:400;color:var(--navy)}
  .reply-card__copy{position:absolute;left:0;width:226px;font-size:4.4px;line-height:5.6px;color:var(--muted)}
  .reply-card__copy--values{top:76px}
  .reply-card__copy--claim{top:107px}
  .fold-hint{position:absolute;left:0;top:186px;font-size:3.4px;color:var(--muted)}
  .fold-line{position:absolute;left:0;top:194px;width:226px;border-top:.6px dashed #aaa}
  .reply-card__heading{position:absolute;left:0;top:206px;font-size:7.4px;font-weight:700;color:#222}
  .reply-card__lead{position:absolute;left:0;top:220px;font-size:4.6px;color:var(--muted)}
  .reply-card__yes{position:absolute;left:0;top:234px;font-size:4.6px;color:var(--muted)}
  .options{position:absolute;left:0;top:243px;list-style:none;font-size:4.6px;line-height:10px;color:var(--muted)}
  .options li{display:flex;align-items:center;gap:3px}
  .options li::before{content:"";width:4px;height:4px;border:.7px solid #333}
  .field{position:absolute;left:0;width:158px;border-top:.6px solid #555;font-size:3.2px;color:var(--muted);padding-top:2px}
</style>
</head>
<body>

<section class="sheet sheet--outside" aria-label="Aussenseite">
  <div class="reply-side">
    <div class="reply-mark">
      <span class="reply-mark__letter">A</span>
      <p class="reply-mark__note">Nicht frankieren<br>Ne pas affranchir<br>Non affrancare</p>
    </div>
    <p class="reply-mark__type">Geschäftsantwortsendung &nbsp;Invio commerciale risposta<br>&nbsp;&nbsp;&nbsp;&nbsp;&nbsp;&nbsp;&nbsp;&nbsp;&nbsp;&nbsp;&nbsp;&nbsp;&nbsp;&nbsp;&nbsp;&nbsp;&nbsp;&nbsp;&nbsp;&nbsp;&nbsp;Envoi commercial-réponse</p>
    <address class="reply-address">NOVERA IMMOBILIEN AG<br>Lindenweg 12<br>8004 Zürich</address>
  </div>

  <div class="cover">
    <div class="brand"><span class="brand__square"></span><span class="brand__name">NOVERA</span></div>
    <div class="cover__photo" role="img" aria-label="Foto: modernes weisses Einfamilienhaus mit beleuchtetem Eingang und Holzsteg in der Abenddämmerung"></div>
    <p class="cover__tagline">Immobilien sind unsere Passion</p>
    <div class="cover__band"><span class="cover__url">novera-haus.ch</span></div>
  </div>
</section>

<section class="sheet sheet--inside" aria-label="Innenseite">
  <div class="services">
    <h2 class="bar bar--services">Unsere Dienstleistung</h2>
    <h3 class="bar bar--sale">Verkauf mit Passion und Sachverstand</h3>
    <p class="copy copy--sale">Der Verkauf einer Immobilie ist ein vielschichtiger Prozess. Lieb gewonnene Liegenschaften, die über viele Jahre ein Zuhause waren, haben für die Verkäufer nicht nur einen Geldwert, sondern auch einen emotionalen Wert. Wir begleiten unsere Kunden mit Passion und Sachverstand durch jede Phase des Verkaufsprozesses.</p>
    <ul class="bullets bullets--sale">
      <li>Erstes Gespräch und Besichtigung der Immobilie</li>
      <li>Ermitteln des bestmöglichen Verkaufspreises</li>
      <li>Erstellen von Verkaufsunterlagen und Vermarktung des Objektes</li>
      <li>Qualifizieren der Kaufinteressenten</li>
      <li>Finanzierungsberatung für Kaufinteressenten</li>
      <li>Preisverhandlungen und ausarbeiten des Kaufvertrags</li>
      <li>Begleitung bei der Beurkundung und Eigentumsübertragung</li>
    </ul>
    <h3 class="bar bar--valuation">Schätzung des Immobilienwerts</h3>
    <p class="copy copy--valuation">Damit unsere Kunden den bestmöglichen Preis für ihr Haus, ihre Eigentumswohnung oder ihr Grundstück erzielen, ermitteln wir den genauen Wert. Unsere Schätzung ergibt eine übersichtliche Aufstellung zum Gebäude, der Lage, dem wirtschaftlichen Wert und Angaben zum Verkehrswert der Immobilie. Wir werden je nach Objekt die folgenden Bewertungsmethoden an:</p>
    <ul class="bullets bullets--valuation">
      <li>Sachwert-, Ertragswert- oder Mischwertmethode</li>
      <li>Hedonische Bewertungen, Residualwertverfahren oder DCF<br>(Discounted-Cash-Flow-Verfahren)</li>
    </ul>
    <div class="brand"><span class="brand__square"></span><span class="brand__name">NOVERA</span></div>
    <address class="contact">NOVERA IMMOBILIEN AG<br>Lindenweg 12<br>8004 Zürich<br>Tel. &nbsp;044 000 12 30<br>Fax &nbsp;044 000 12 31<br>info@novera-haus.ch<br>www.novera-haus.ch</address>
  </div>

  <div class="perforation" aria-hidden="true"></div>

  <div class="reply-card">
    <div class="tape tape--top">Klebestreifen</div>
    <h3 class="reply-card__title">Unsere Werte und Visionen</h3>
    <p class="reply-card__copy reply-card__copy--values">Jede Immobilie ist so einzigartig, wie die Menschen, denen sie gehört. Für uns zählt der Mensch, die Liegenschaft und die gemeinsame Geschichte. In über 20 Jahren haben wir das Immobiliengeschäft und all seine Facetten verinnerlicht. Das macht uns zu einem kompetenten und engagierten Partner für alle Fragen rund um Immobilien.</p>
    <p class="reply-card__copy reply-card__copy--claim">Immobilien sind unsere Passion und die Zufriedenheit der Kunden ist unser Ziel.</p>
    <p class="fold-hint">(Bitte 1x falten)</p>
    <div class="fold-line" aria-hidden="true"></div>
    <h3 class="reply-card__heading">Rückantwort</h3>
    <p class="reply-card__lead">Bitte kreuzen Sie Ihre Wünsche an:</p>
    <p class="reply-card__yes">Ja,</p>
    <ul class="options">
      <li>…wir denken über einen Verkauf unserer Immobilie nach</li>
      <li>…wir sind am Kauf einer Wohnung/Haus interessiert</li>
      <li>…wir wünschen ein unverbindliches persönliches Gespräch</li>
    </ul>
    <div class="field" style="top:284px">Name / Vorname</div>
    <div class="field" style="top:302px">Strasse / Nr.</div>
    <div class="field" style="top:320px">PLZ / Ort</div>
    <div class="field" style="top:339px">Telefon</div>
    <div class="field" style="top:357px">E-Mail</div>
    <div class="tape tape--bottom">Klebestreifen</div>
  </div>
</section>

</body>
</html>
```